BRIGHT COLORFUL + 55 FAMILY HISTORY BROCHURE 11 x 17 bifold

11 x 17 Bifold Flyer I have given you the Layout I just need you to make it Pretty

YOU DO NOT NEED TO FOLLOW MY LAYOUT, You can but dont have too

Target Market(s)

55 year old consumers, who could choose our service of Hereditary Cancer Screening

Industry/Entity Type

Health And Wellness

Requirements
Must have
• Must be appealing to Grand Parents, must make them want to test , show lots of pictures of grand children, YOU DO NOT NEED TO FOLLOW MY LAYOUT , You can but dont have too
Nice to have
• use our colors of our logo , YOU DO NOT NEED TO FOLLOW MY LAYOUT , You can but dont have too
Should not have
• YOU DO NOT NEED TO FOLLOW MY LAYOUT, You can but dont have too

```html
<!DOCTYPE html>
<html lang="en">
<head>
<meta charset="utf-8">
<title>Family History Brochure</title>
<link href="https://fonts.googleapis.com/css2?family=Didact+Gothic&family=Oswald:wght@600&display=swap" rel="stylesheet">
<style>
  :root{
    --green:#8cc63f;
    --ink:#1f1f1f;
    --white:#ffffff;
    --rule:#1a1a1a;
    --photo-warm-a:#c98b5a;
    --photo-warm-b:#e9d3b0;
    --photo-green-a:#6f9a4a;
    --photo-green-b:#c7c2b6;
  }
  *{margin:0;padding:0;box-sizing:border-box}
  html,body{width:1200px;height:812px;overflow:hidden;background:var(--white)}
  body{position:relative;font-family:"Didact Gothic",sans-serif;color:var(--ink)}
  .top-rule{position:absolute;left:0;top:0;width:1200px;height:3px;background:var(--rule)}
  .fold-rule{position:absolute;left:598px;top:0;width:3px;height:778px;background:var(--rule)}

  .panel{position:absolute;background:var(--green);border-radius:8px}
  .panel--left{left:22px;top:20px;width:558px;height:772px}
  .panel--right{left:623px;top:23px;width:556px;height:771px}

  .sheet{position:absolute;background:var(--white)}
  .panel--left .sheet{left:5px;top:6px;width:548px;height:534px}
  .panel--right .sheet{left:5px;top:230px;width:546px;height:536px;border-radius:0 0 6px 6px}

  .copy{position:absolute;font-size:13.2px;line-height:16.5px;text-align:justify}
  .copy b{font-weight:700}
  .story-1{left:24px;top:13px;width:500px}
  .story-2{left:24px;top:97px;width:500px}
  .story-3{left:24px;top:247px;width:500px}
  .story-4{left:24px;top:419px;width:500px}

  .photo{position:absolute;border:3px solid var(--white)}
  .photo--family{left:12px;top:570px;width:216px;height:168px;
    background:linear-gradient(135deg,var(--photo-warm-a),var(--photo-warm-b) 60%,var(--photo-green-a))}
  .photo--grandpa{left:311px;top:40px;width:224px;height:151px;
    background:linear-gradient(120deg,var(--photo-green-a),var(--photo-green-b) 55%,#9a8d80)}

  .callout{position:absolute;left:242px;top:573px;width:300px;color:var(--white);font-size:19.5px;line-height:23.6px}
  .callout b{font-weight:700;letter-spacing:.3px}

  .site{position:absolute;left:0;width:100%;text-align:center;font-size:10px;letter-spacing:1.4px;color:var(--ink)}
  .panel--left .site{top:755px}
  .panel--right .sheet .site{top:516px}

  .cover-title{position:absolute;left:14px;top:63px;color:var(--white);font-size:21.5px;font-weight:700;letter-spacing:.4px}
  .cover-sub{position:absolute;left:14px;top:120px;width:290px;color:var(--white);font-size:19.5px;line-height:24px}

  .info-1{left:25px;top:27px;width:494px}
  .info-2{left:25px;top:111px;width:494px}
  .info-3{left:25px;top:247px;width:494px}

  .headline{position:absolute;left:10px;top:404px;width:526px;text-align:center;color:var(--green);
    font-family:"Oswald",sans-serif;font-weight:600;font-size:32px;line-height:39px;letter-spacing:-.3px}
</style>
</head>
<body>
  <div class="top-rule"></div>
  <div class="fold-rule"></div>

  <section class="panel panel--left">
    <div class="sheet">
      <p class="copy story-1"><b>Genetic testing revealed</b> Daniel Hartman carried a mutation that gave him a 55 to 70 percent chance of developing stomach cancer. Early screening revealed there were 14 sites of stage 1A cancer. Once the news sunk in, he realized <b>his Mother Genetic Testing Saved His Life.</b></p>
      <p class="copy story-2"><b>Genetic Testing Saved My Life,</b> Because of my age and <b>Ashkenazi Jewish ancestry,</b> My Dr recommended Genetic Testing and they were right. I had the BRCA Gene, because of this my other two sister got tested, my younger sister was positive and my older sister was negative. <b>Now we are in control,</b> there are steps that can be taken to reduce the risks, including enhanced breast cancer screening, risk-reducing surgeries, and chemoprevention, in which drugs are used to try to reduce the risk or delay the development of cancer.</p>
      <p class="copy story-3"><b>A breast cancer survivor before age 30:</b> ‘Genetic testing saved my life’ Megan Cole was diagnosed with breast cancer two weeks before her 29th birthday. Cole, now 30, credits her recovery to <b>awareness</b> of a <b>hereditary genetic mutation</b> that predisposed her and her family to the disease. <b>After my mom tested positive for the BRCA 1 gene mutation,</b> I knew genetic testing was something that I would need. <b>Once I tested positive,</b> I was referred to a breast health clinic for <b>increased surveillance.</b> There, my medical care providers were very diligent in making sure I was watched closely. <b>Knowledge is power</b> and, in this case, <b>Genetic testing saved my life!</b></p>
      <p class="copy story-4"><b>My father had genetic testing</b> and found he had hereditary nonpolyposis colorectal cancer (HNPCC) commonly known as Lynch syndrome. My name is Laura Whitfield and I am a 10-year survivor of colorectal cancer. From an early age I learned the importance of screenings and knew about signs and symptoms. <b>Following screening guidelines for individuals at an increased risk &amp; Knowing my family history saved my life!</b></p>
    </div>
    <div class="photo photo--family" role="img" aria-label="Photo of a grandmother, mother and toddler smiling together"></div>
    <p class="callout">A Positive result or finding a mutation is Not a Cancer Diagnosis and does not mean you will ever develop Cancer <b>Learning if you have an increased risk for cancer can make a difference.</b></p>
    <p class="site">www.kinshipScreening.com</p>
  </section>

  <section class="panel panel--right">
    <h1 class="cover-title">“The Power of Knowledge”</h1>
    <p class="cover-sub">Helping Younger Family Members Know if there is a Risk and Preparing them for it.</p>
    <div class="photo photo--grandpa" role="img" aria-label="Photo of a grandfather hugging his young grandson outdoors"></div>
    <div class="sheet">
      <p class="copy info-1"><b>Genetic Testing</b> is done to determine whether family members without obvious illness have inherited the same mutation as a family member who is known to carry a cancer associated mutation. Meaning <b>Will You Help Your Kids &amp; Grand Children.</b></p>
      <p class="copy info-2"><b>What are the benefits of testing?</b> “The Power of Knowledge” <b>Helping Younger Family Members Know if there is a Risk and Preparing for it.</b> knowing if you have a genetic mutation is that you can work with your doctor to monitor and address your cancer risks. <b>According to the National Wellness Council eating 5 or more Servings of Vegetables &amp; Fruit, and Most Importantly also lowering your intake of red meat, dairy and eggs will help prevent or delay cancer.</b></p>
      <p class="copy info-3"><b>There are many benefits to getting tested,</b> regardless of the eventual result. If one of your family members — however distant — had cancer, there is a chance that you inherited a gene mutation that not only increases your personal risk of cancer, but also could be passed to the next generation. Those who are carriers of hereditary cancer gene mutations, could be at risk of getting cancer earlier in life than the general population. <b>The sooner genetic testing is done, the more likely it is that the risk can be managed appropriately.</b></p>
      <h2 class="headline">There are many Known risk factors for Cancer. GENETICS and FAMILY HISTORY</h2>
      <p class="site">www.kinshipScreening.com</p>
    </div>
  </section>
</body>
</html>
```